Illustrate timeline of pregnancy with 4 stages of testing

I am looking for a graphical representation of a testing map for mothers milk (or mothers blood before birth).

We are testing mothers milk for nutrients at up to 4 stages during pregnancy.. Maybe before birth (optional).. At 1 month age, at 3 months age and at 5 months age.

A mother can have the test at all stages, or she can test at some stages.. Or only one stage.

This „map“ should show a kind of timeline from last trimester.. To birth.. To the baby age of 12 months. It would also be good to show how long breast feeding is done (12 months minimum.. Up to 2 years) and when to start with solid food (at 6 months age).

The results of a test are always shown as a bar with green (ok) organe (low) and Red (Very Low) where the arrow shows the position. I can not change the design or orientation of the bars (hardcoded).... I can only change the color.... to grey or other colors if necessary. The rest is flexible.

Design should be feminime.. soft... baby-themed.

Please do a timeline from the top towards the bottom... not horizontally.

A rough content map is shown.

ATENTION!!! I am a heavy user of Gigbarrow (More than 150 projects done so far) and I am looking for good people to work with long term. This is why I would like to give you future projects if this is going well. For this.. proficiency in Indesign and Photoshop is ESSENTIAL! Please do not bid if you can not use these programs.

Thanks!

```html
<!DOCTYPE html>
<html lang="en">
<head>
<meta charset="utf-8">
<title>Breast Milk Testing Timeline</title>
<link rel="stylesheet" href="https://fonts.googleapis.com/css2?family=Montserrat:wght@600;700;800&family=Nunito:wght@800;900&display=swap">
<style>
  :root {
    --plum: #9b3a63;
    --plum-dark: #8d3558;
    --rose: #cf4f82;
    --rose-number: #c9457a;
    --bubble: #f4a6c8;
    --rule: #f4c3d6;
    --rule-lilac: #d9c6e6;
    --milk-blue: #78ace0;
    --milk-text: #a3c3e8;
    --food-orange: #f4a262;
    --food-text: #f8c23a;
    --white: #ffffff;
  }
  * { margin: 0; padding: 0; box-sizing: border-box; }
  html, body { width: 1200px; height: 2386px; overflow: hidden; background: var(--white); }
  .poster { position: relative; width: 1200px; height: 2386px; font-family: "Montserrat", Arial, sans-serif; }
  .timeline-art { position: absolute; inset: 0; }
  .stage-banner {
    position: absolute; left: 359px; top: 24px; width: 478px; height: 73px;
    background: var(--plum); color: var(--white);
    clip-path: polygon(0 0, 100% 0, 94% 50%, 100% 100%, 0 100%, 6% 50%);
    display: flex; align-items: center; justify-content: center;
    font-weight: 600; font-size: 40px;
  }
  .headline {
    position: absolute; top: 170px; font-weight: 800; font-size: 244px;
    line-height: 1; color: var(--rose); letter-spacing: 6px;
  }
  .headline--start { left: 206px; }
  .headline--end { left: 706px; }
  .newborn {
    position: absolute; left: 520px; top: 80px; width: 190px; height: 354px;
    border-radius: 40%;
    background: radial-gradient(ellipse at center, #f7dcc2 0%, #fbeec6 45%, rgba(255,250,220,0) 72%);
  }
  .months-label {
    position: absolute; left: 560px; top: 434px; width: 80px; text-align: center;
    font-size: 14px; font-weight: 600; color: var(--rose);
  }
  .feed-label {
    position: absolute; font-family: "Nunito", Arial, sans-serif; font-weight: 900;
    font-size: 58px; line-height: 1.0;
  }
  .feed-label--milk { left: 62px; top: 968px; color: var(--milk-text); }
  .feed-label--food { left: 932px; top: 1228px; color: var(--food-text); }
  .food-bowl {
    position: absolute; left: 948px; top: 1462px; width: 252px; height: 454px;
    background: radial-gradient(ellipse at 70% 62%, #f7a81c 0%, #f7b52a 32%, #e9e9e9 33%, #dddddd 55%, rgba(255,255,255,0) 70%);
  }
  .birthday-cake {
    position: absolute; left: 583px; top: 1562px; width: 34px; height: 56px;
    border-radius: 6px; background: linear-gradient(#78c9c0 0%, #78c9c0 55%, #6b4a3a 56%, #6b4a3a 100%);
  }
  .results-panel {
    position: absolute; left: 0; top: 2168px; width: 1200px; height: 218px;
    background: var(--plum-dark); color: var(--white);
  }
  .result { position: absolute; width: 560px; height: 70px; }
  .result__name { position: absolute; left: 10px; top: 0; font-size: 15px; font-weight: 600; }
  .result__bar {
    position: absolute; left: 0; top: 20px; width: 438px; height: 22px;
    border-radius: 11px; border: 2px solid #f2e6ec;
  }
  .result__bar--grey { background: linear-gradient(90deg, #4a4a4a, #bdbdbd 50%, #8d8d8d); }
  .result__bar--scale { background: linear-gradient(90deg, #d9262b, #f39b2f 50%, #6cbf4b); }
  .result__marker { position: absolute; top: 26px; width: 4px; height: 30px; background: #111; }
  .result__marker::after {
    content: ""; position: absolute; left: -5px; bottom: 0; width: 14px; height: 12px; background: #111;
  }
  .result__value { position: absolute; left: 452px; top: 18px; font-size: 19px; font-weight: 600; white-space: nowrap; }
  .result__value--pct { font-size: 22px; top: 15px; }
</style>
</head>
<body>
<main class="poster">

  <svg class="timeline-art" width="1200" height="2386" viewBox="0 0 1200 2386" aria-hidden="true">
    <g class="rules" stroke="var(--rule)" stroke-width="2">
      <line x1="0" y1="480" x2="1200" y2="480"/>
      <line x1="0" y1="537" x2="1200" y2="537"/>
      <line x1="0" y1="597" x2="1200" y2="597"/>
      <line x1="0" y1="672" x2="1200" y2="672"/>
      <line x1="0" y1="758" x2="1200" y2="758"/>
      <line x1="0" y1="853" x2="1200" y2="853"/>
      <line x1="0" y1="964" x2="1200" y2="964"/>
      <line x1="0" y1="1075" x2="1200" y2="1075"/>
      <line x1="0" y1="1196" x2="1200" y2="1196"/>
      <line x1="0" y1="1329" x2="1200" y2="1329"/>
      <line x1="0" y1="1468" x2="1200" y2="1468"/>
      <line x1="0" y1="1620" x2="1000" y2="1620"/>
      <line x1="0" y1="1785" x2="1200" y2="1785" stroke="var(--rule-lilac)"/>
      <line x1="0" y1="1981" x2="1200" y2="1981" stroke="var(--rule-lilac)"/>
    </g>

    <line class="stem" x1="599" y1="470" x2="599" y2="2168" stroke="var(--bubble)" stroke-width="12"/>

    <g class="brace brace--milk" fill="none" stroke="var(--milk-blue)" stroke-width="5" stroke-dasharray="14 9">
      <path d="M575 480 H450 Q395 480 395 535 V1005 Q395 1057 298 1057 Q395 1057 395 1110 V1570 Q395 1620 450 1620 H530"/>
      <path d="M530 1620 H450 Q395 1620 395 1670 V1955 Q395 2005 450 2005 H500"/>
    </g>
    <g class="brace brace--food" fill="none" stroke="var(--food-orange)" stroke-width="5" stroke-dasharray="14 9">
      <path d="M655 955 H755 Q810 955 810 1010 V1240 Q810 1291 900 1291 Q810 1291 810 1342 V1570 Q810 1620 755 1620 H672"/>
      <path d="M672 1620 H735 Q790 1620 790 1670 V1955 Q790 2005 735 2005 H718"/>
    </g>

    <path class="milk-drop" d="M153 810 C135 850 105 880 105 910 A48 48 0 0 0 201 910 C201 880 171 850 153 810 Z" fill="var(--milk-text)"/>

    <g class="month-bubbles" fill="var(--bubble)">
      <circle cx="599" cy="480" r="22"/>
      <circle cx="599" cy="537" r="24"/>
      <circle cx="599" cy="597" r="30"/>
      <circle cx="599" cy="672" r="36"/>
      <circle cx="599" cy="758" r="42"/>
      <circle cx="599" cy="853" r="46"/>
      <circle cx="599" cy="960" r="52"/>
      <circle cx="599" cy="1073" r="58"/>
      <circle cx="599" cy="1196" r="63"/>
      <circle cx="599" cy="1329" r="67"/>
      <circle cx="599" cy="1468" r="71"/>
      <circle cx="599" cy="1620" r="73"/>
      <circle cx="599" cy="1785" r="81"/>
      <circle cx="599" cy="1981" r="103"/>
    </g>
    <g class="month-numbers" fill="var(--rose-number)" font-family="Montserrat, Arial, sans-serif" font-weight="700" text-anchor="middle">
      <text x="599" y="488" font-size="24">1</text>
      <text x="599" y="546" font-size="26">2</text>
      <text x="599" y="609" font-size="34">3</text>
      <text x="599" y="686" font-size="40">4</text>
      <text x="599" y="774" font-size="46">5</text>
      <text x="599" y="871" font-size="50">6</text>
      <text x="599" y="981" font-size="58">7</text>
      <text x="599" y="1096" font-size="62">8</text>
      <text x="599" y="1221" font-size="68">9</text>
      <text x="599" y="1354" font-size="66">10</text>
      <text x="599" y="1493" font-size="66">11</text>
      <text x="599" y="1654" font-size="15" font-weight="600">1st Birthday</text>
      <text x="599" y="1786" font-size="50">1.5</text>
      <text x="599" y="1820" font-size="28">Years old</text>
      <text x="599" y="1990" font-size="74">2</text>
      <text x="599" y="2030" font-size="32">Years old</text>
    </g>
  </svg>

  <div class="stage-banner">3rd Trimester</div>
  <div class="headline headline--start">BIR</div>
  <div class="headline headline--end">TH</div>
  <div class="newborn" role="img" aria-label="Illustration of a smiling newborn baby in a nappy, glowing at birth"></div>
  <div class="months-label">Months</div>

  <div class="feed-label feed-label--milk">Breast<br>Milk</div>
  <div class="feed-label feed-label--food">Solid<br>food</div>

  <div class="food-bowl" role="img" aria-label="Illustration of a bowl of orange baby food with a spoon"></div>
  <div class="birthday-cake" role="img" aria-label="Small birthday cake with a number one candle"></div>

  <section class="results-panel">
    <div class="result" style="left:50px; top:34px;">
      <span class="result__name">Optional Pre-Test</span>
      <div class="result__bar result__bar--grey"></div>
      <span class="result__marker" style="left:22px;"></span>
      <span class="result__value">Not tested</span>
    </div>
    <div class="result" style="left:50px; top:128px;">
      <span class="result__name">Primary testing</span>
      <div class="result__bar result__bar--scale"></div>
      <span class="result__marker" style="left:166px;"></span>
      <span class="result__value result__value--pct">55%</span>
    </div>
    <div class="result" style="left:629px; top:34px;">
      <span class="result__name">Secondary testing</span>
      <div class="result__bar result__bar--scale"></div>
      <span class="result__marker" style="left:196px;"></span>
      <span class="result__value result__value--pct">92%</span>
    </div>
    <div class="result" style="left:629px; top:128px;">
      <span class="result__name">Tertiary testing</span>
      <div class="result__bar result__bar--grey"></div>
      <span class="result__marker" style="left:16px;"></span>
      <span class="result__value">Not tested</span>
    </div>
  </section>

</main>
</body>
</html>
```